Business needs Office Posters Designed

I need a office poster designed to put on a 2 feet x 3 feet space:
My Employee is Better Than Me.
- to signify the importance of listening to your employees, because they know better, more experienced in their respective fields.

Target Market(s)

employees

Industry/Entity Type

Healthcare

```html
<!DOCTYPE html>
<html lang="en">
<head>
<meta charset="utf-8">
<title>My Employee Is Better Than Me — Office Poster</title>
<link rel="stylesheet" href="https://fonts.googleapis.com/css2?family=Bebas+Neue&display=swap">
<style>
  :root {
    --paper: #ffffff;
    --navy: #0b0b6b;
    --red: #b80024;
    --ribbon-text: #ffffff;
  }
  html, body {
    margin: 0;
    padding: 0;
    width: 800px;
    height: 1200px;
    overflow: hidden;
    background: var(--paper);
  }
  .poster {
    display: block;
    width: 800px;
    height: 1200px;
  }
  .headline {
    font-family: "Bebas Neue", "Oswald", sans-serif;
    text-anchor: middle;
  }
  .headline--navy { fill: var(--navy); }
  .headline--red { fill: var(--red); }
  .headline--on-ribbon { fill: var(--ribbon-text); }
  .ribbon { fill: var(--red); }
  .star { fill: var(--navy); }
</style>
</head>
<body>
<svg class="poster" viewBox="0 0 800 1200" xmlns="http://www.w3.org/2000/svg" role="img" aria-label="My employee is better than me.">
  <defs>
    <polygon id="star-shape" points="0,-17 4,-5.5 16.2,-5.3 6.5,2.1 10,13.8 0,6.8 -10,13.8 -6.5,2.1 -16.2,-5.3 -4,-5.5"/>
  </defs>

  <rect width="800" height="1200" fill="var(--paper)"/>

  <text class="headline headline--navy" x="400" y="277" font-size="160">MY</text>

  <polygon class="ribbon" points="84,309 719,309 683,368 719,427 84,427 120,368"/>
  <text class="headline headline--on-ribbon" x="402" y="421" font-size="133" letter-spacing="3">EMPLOYEE</text>

  <g class="stars stars--left">
    <use href="#star-shape" class="star" x="184" y="520"/>
    <use href="#star-shape" class="star" x="237" y="520"/>
    <use href="#star-shape" class="star" x="290" y="520"/>
  </g>
  <text class="headline headline--navy" x="400" y="572" font-size="136">IS</text>
  <g class="stars stars--right">
    <use href="#star-shape" class="star" x="484" y="520"/>
    <use href="#star-shape" class="star" x="537" y="520"/>
    <use href="#star-shape" class="star" x="590" y="520"/>
  </g>

  <text class="headline headline--navy" x="400" y="723" font-size="160">BETTER</text>
  <text class="headline headline--navy" x="400" y="858" font-size="160">THAN</text>
  <text class="headline headline--red" x="405" y="1020" font-size="160">ME.</text>
</svg>
</body>
</html>
```